PLUM BUSINESS CARD

Need a business card and logo. The company name is PLUM (Piedmont League of Ultimate Mareriders). It's a business that offers horseback riding lessons to young girls. Please put my name: Renata Bowley and a place for email and phone number. I would like the card to look feminine and soft. I like script type lettering. I want the card to be white or ivory with black or gray and hot pink print. A horse head outline would be cool, something whimsical. Think teen girl who likes glamour. Also, I give western riding lessons. So I like faded out background Images of western saddles, cowgirls, horses with long hair, ropes, horses in sunset...mabe the word PLUM can be made out of a lasso rope?

Just updated my project with a little more detail

Target Market(s)

Young girls/ cowgirls, western riding

Industry/Entity Type

Horseback Riding

Font styles to use
Script

Colors
e34197

Requirements
Must have
• A logo of PLUM.
Must say Piedmont League of Ultimate Mareriders
Colors are Pink and Black with an elegant, glamorous, feminine look.
Nice to have
• Could have a picture or outline of a horse

```html
<!DOCTYPE html>
<html lang="en">
<head>
<meta charset="utf-8">
<title>PLUM Business Card</title>
<link rel="stylesheet" href="https://fonts.googleapis.com/css2?family=Questrial&family=Montserrat:wght@700&display=swap">
<style>
  :root {
    --card-black: #050505;
    --hot-pink: #e34197;
    --band-pink: #e94fd6;
    --white: #ffffff;
    --backdrop: #e9e6e2;
    --photo-stone: #8a8470;
    --photo-green: #4f6e2c;
    --photo-chestnut: #6e2414;
  }
  * { box-sizing: border-box; margin: 0; padding: 0; }
  html, body {
    width: 1200px; height: 1000px; overflow: hidden;
    background: var(--backdrop);
  }
  .canvas {
    position: relative; width: 1200px; height: 1000px;
    display: flex; align-items: center; justify-content: center;
  }
  .card {
    position: relative; width: 1000px; height: 600px;
    background: var(--card-black); border-radius: 40px; overflow: hidden;
    font-family: "Questrial", "Century Gothic", sans-serif; color: var(--white);
  }
  .brand {
    position: absolute; top: 38px; left: 0; right: 0;
    display: flex; align-items: center; justify-content: center; gap: 22px;
  }
  .brand-dot {
    width: 64px; height: 64px; border-radius: 50%;
    border: 4px solid var(--band-pink);
  }
  .brand-name { font-size: 80px; letter-spacing: 2px; line-height: 1; }
  .band {
    position: absolute; left: 0; right: 0; height: 44px;
    background: var(--band-pink);
    display: flex; align-items: center; justify-content: center;
    font-size: 32px; color: var(--white); letter-spacing: 0.5px;
  }
  .band-league { top: 150px; }
  .band-tagline { top: 366px; }
  .photo-strip {
    position: absolute; top: 194px; left: 0; right: 0; height: 172px;
    display: flex;
  }
  .photo { height: 100%; }
  .photo-kiss { width: 210px; background: linear-gradient(135deg, var(--photo-stone), #2e2a3e); }
  .photo-rider { width: 330px; background: linear-gradient(160deg, var(--photo-green), #d9d6cf 70%); }
  .photo-jump { flex: 1; background: linear-gradient(120deg, var(--photo-chestnut), #a7b1a9 80%); }
  .contact-phone {
    position: absolute; left: 40px; top: 448px;
    display: flex; align-items: center; gap: 10px; font-size: 30px;
  }
  .holder-name {
    position: absolute; left: 0; right: 0; top: 440px; text-align: center;
    font-family: "Montserrat", "Arial", sans-serif; font-weight: 700;
    font-size: 32px; color: var(--band-pink);
  }
  .contact-email {
    position: absolute; right: 40px; top: 520px;
    display: flex; align-items: center; gap: 10px; font-size: 30px;
  }
</style>
</head>
<body>
<main class="canvas">
  <article class="card">
    <header class="brand">
      <span class="brand-dot"></span>
      <span class="brand-name">PLUM</span>
    </header>

    <div class="band band-league">Piedmont League of Ultimate Mareriders</div>

    <div class="photo-strip">
      <div class="photo photo-kiss" role="img" aria-label="Girl hugging a brown pony beside a stone wall"></div>
      <div class="photo photo-rider" role="img" aria-label="Young girl in pink riding a grey horse in a green paddock"></div>
      <div class="photo photo-jump" role="img" aria-label="Rider on a chestnut horse taking a jump"></div>
    </div>

    <div class="band band-tagline">Horseback riding lessons to yong girls</div>

    <div class="contact-phone">
      <svg width="20" height="32" viewBox="0 0 20 32" aria-hidden="true">
        <rect x="2" y="2" width="16" height="28" rx="3" fill="none" stroke="#e94fd6" stroke-width="3"/>
        <line x1="7" y1="25" x2="13" y2="25" stroke="#e94fd6" stroke-width="2"/>
      </svg>
      <span>0412557308</span>
    </div>

    <div class="holder-name">Renata Bowley</div>

    <div class="contact-email">
      <span>hello@plumriders.net</span>
      <svg width="30" height="22" viewBox="0 0 30 22" aria-hidden="true">
        <rect x="1.5" y="1.5" width="27" height="19" fill="none" stroke="#e94fd6" stroke-width="2.5"/>
        <polyline points="1.5,1.5 15,12 28.5,1.5" fill="none" stroke="#e94fd6" stroke-width="2.5"/>
      </svg>
    </div>
  </article>
</main>
</body>
</html>
```